Business Cards that are elegant and wow

I want to create and print business cards that represent my brand and stand out from the rest. We want to ensure they stay in our branding and the integrity is not lost. I am happy to look at different shapes like square etc.

It will be printed on very thick cards and will be stylish .

I want to create and print business cards that represent my brand and stand out from the rest. We want to ensure they stay in ur branding and the integrity is not lost. I am happy to look at different shapes like square etc.

Target Market(s)

real estate professionals

Industry/Entity Type

Real Estate

Contact Information for Business Card

Wren Holt
hello@bramblecovehomes.com.au
bramblecovehomes.com.au
0417 382 906 (SMS)

Colors

Designer to choose colors to be used in the design.

Requirements
Must have
• My logo
• email
• website
• Name
Nice to have
• I like the idea of printing with foil or spot gloss. You want it to stand out in a sea.
Should not have
• I would like you to stay in my colour themes. Don't change the colour of my logo

```html
<!DOCTYPE html>
<html lang="en">
<head>
<meta charset="utf-8">
<title>Bramble Cove Homes – Business Cards</title>
<link rel="stylesheet" href="https://fonts.googleapis.com/css2?family=Montserrat:wght@600&family=Oswald:wght@500&family=Open+Sans:wght@400&display=swap">
<style>
  :root {
    --backdrop: #3a3a3c;
    --card: #1c1c1d;
    --card-edge: #111112;
    --cyan: #29b6ee;
    --pink: #ec2a7f;
    --white: #f4f4f4;
    --muted: #d9d9d9;
  }
  * { box-sizing: border-box; margin: 0; padding: 0; }
  html, body {
    width: 1200px; height: 1200px; overflow: hidden;
    background: var(--backdrop);
  }
  .canvas {
    position: relative; width: 1200px; height: 1200px;
  }
  .card {
    position: absolute; left: 150px; width: 900px; height: 514px;
    background: var(--card);
    border-radius: 34px;
    overflow: hidden;
    box-shadow: 0 10px 30px rgba(0,0,0,.45);
  }
  .card--front { top: 50px; }
  .card--back { top: 636px; }

  .brand {
    position: absolute; display: flex; align-items: center; gap: 22px;
  }
  .brand__mark {
    width: 96px; height: 96px; border-radius: 50%;
    border: 7px solid var(--pink); flex: none;
  }
  .brand__name {
    font-family: "Montserrat", sans-serif; font-weight: 600;
    color: var(--cyan); font-size: 46px; line-height: 1.05;
    letter-spacing: 1px; text-transform: uppercase;
  }
  .card--front .brand { left: 50%; top: 50%; transform: translate(-50%, -50%); }
  .card--back .brand { left: 60px; top: 110px; }
  .card--back .brand__mark { width: 82px; height: 82px; border-width: 6px; }
  .card--back .brand__name { font-size: 36px; }

  .contact {
    position: absolute; left: 480px; top: 230px;
  }
  .contact__name {
    font-family: "Oswald", sans-serif; font-weight: 500;
    font-size: 42px; letter-spacing: .5px; color: var(--white);
    text-transform: uppercase; line-height: 1.1; margin-bottom: 10px;
  }
  .contact__name span { color: var(--cyan); }
  .contact__list { list-style: none; }
  .contact__item {
    display: flex; align-items: center; gap: 12px;
    font-family: "Open Sans", sans-serif; font-size: 19px;
    color: var(--muted); line-height: 1.55;
  }
  .contact__icon { width: 16px; height: 16px; flex: none; }

  .edge-band {
    position: absolute; right: 0; top: 150px; width: 16px; bottom: 0;
    background: var(--cyan);
  }
  .edge-band--top {
    top: 0; height: 150px; width: 16px;
    background: linear-gradient(to top, var(--pink), rgba(236,42,127,.2));
  }
  .base-band {
    position: absolute; bottom: 0; left: 320px; right: 16px; height: 16px;
    background: linear-gradient(to right, rgba(236,42,127,0), var(--pink));
  }
</style>
</head>
<body>
<main class="canvas">

  <section class="card card--front" aria-label="Card front">
    <div class="brand">
      <span class="brand__mark"></span>
      <span class="brand__name">Bramble Cove Homes</span>
    </div>
  </section>

  <section class="card card--back" aria-label="Card back">
    <div class="brand">
      <span class="brand__mark"></span>
      <span class="brand__name">Bramble Cove Homes</span>
    </div>

    <div class="contact">
      <h1 class="contact__name">Wren <span>Holt</span></h1>
      <ul class="contact__list">
        <li class="contact__item">
          <svg class="contact__icon" viewBox="0 0 16 16"><path fill="#ec2a7f" d="M3.5 1.5l2.5 0 1 3.5-1.7 1.2a8 8 0 0 0 4.5 4.5L11 9l3.5 1v2.5c0 1-1 2-2 2A11 11 0 0 1 1.5 3.5c0-1 1-2 2-2z"/></svg>
          +0417-382-906 (SMS)
        </li>
        <li class="contact__item">
          <svg class="contact__icon" viewBox="0 0 16 16"><rect x="1" y="3" width="14" height="10" rx="1.5" fill="#ec2a7f"/><path d="M1.5 4l6.5 5 6.5-5" fill="none" stroke="#1c1c1d" stroke-width="1.4"/></svg>
          hello@bramblecovehomes.com.au
        </li>
        <li class="contact__item">
          <svg class="contact__icon" viewBox="0 0 16 16"><g fill="none" stroke="#ec2a7f" stroke-width="1.4"><circle cx="8" cy="8" r="6.5"/><ellipse cx="8" cy="8" rx="3" ry="6.5"/><path d="M1.5 8h13"/></g></svg>
          bramblecovehomes.com.au
        </li>
      </ul>
    </div>

    <div class="edge-band edge-band--top" role="img" aria-label="Pink accent strip fading along the top of the right edge"></div>
    <div class="edge-band"></div>
    <div class="base-band" role="img" aria-label="Pink accent strip fading along the bottom edge"></div>
  </section>

</main>
</body>
</html>
```